morvel family medicine business cards

create business cards for 7 family medicine providers and 4 admin using attached logo
2 locations
appointment reminder on back of cards
will provide more info regarding names,addresses, credentials etc once started

```html
<!DOCTYPE html>
<html lang="en">
<head>
<meta charset="utf-8">
<title>Morvel Family Medicine – Business Cards</title>
<link rel="stylesheet" href="https://fonts.googleapis.com/css2?family=Open+Sans:wght@400;600;700&display=swap">
<style>
  :root {
    --bg: #2b2b2b;
    --card: #ffffff;
    --accent: #29a6de;
    --navy: #2a2466;
    --ink: #2e2e2e;
    --rule: #222222;
  }
  * { margin: 0; padding: 0; box-sizing: border-box; }
  html, body { width: 1200px; height: 1059px; overflow: hidden; }
  body {
    background: var(--bg);
    font-family: "Open Sans", sans-serif;
    color: var(--ink);
    position: relative;
  }
  .card {
    position: absolute;
    left: 254px;
    width: 692px;
    height: 392px;
    background: var(--card);
    border-radius: 22px;
  }
  .card-front { top: 88px; }
  .card-back { top: 546px; }

  .provider-name {
    position: absolute; left: 26px; top: 20px;
    font-size: 30px; font-weight: 700; color: var(--accent);
    letter-spacing: 0.1px;
  }
  .staff-list {
    position: absolute; left: 26px; top: 56px;
    list-style: none; font-size: 16px; line-height: 24.5px;
  }
  .brand {
    position: absolute; left: 453px; top: 24px; width: 216px; height: 182px;
    display: flex; flex-direction: column; align-items: center; justify-content: center; gap: 14px;
  }
  .brand-dot { width: 96px; height: 96px; border-radius: 50%; background: var(--accent); }
  .brand-name {
    font-size: 18px; font-weight: 600; color: var(--navy);
    text-align: center; line-height: 1.2; white-space: nowrap;
  }

  .location {
    position: absolute; top: 232px;
    font-size: 19px; line-height: 24px; font-style: normal;
  }
  .location-primary { left: 26px; }
  .location-secondary { right: 22px; text-align: right; }
  .contact { position: absolute; top: 294px; list-style: none; font-size: 19px; line-height: 24.5px; }
  .contact-left { left: 26px; }
  .contact-right { right: 22px; text-align: right; }
  .contact li { display: flex; align-items: center; gap: 8px; }
  .contact-right li { justify-content: flex-end; }
  .icon { width: 18px; height: 18px; fill: var(--accent); flex: none; }

  .reminder-title {
    position: absolute; top: 28px; width: 100%; text-align: center;
    font-size: 21px; font-weight: 600;
  }
  .field { position: absolute; left: 0; width: 100%; height: 30px; }
  .field-label {
    position: absolute; right: 530px; bottom: 0;
    font-size: 21px; font-weight: 600; line-height: 1;
  }
  .field-line {
    position: absolute; left: 168px; width: 438px; bottom: 2px;
    border-bottom: 1.5px solid var(--rule);
  }
  .field-name { top: 120px; }
  .field-date { top: 181px; }
  .field-time { top: 241px; }
  .cancel-note {
    position: absolute; top: 340px; width: 100%; text-align: center; font-size: 16.5px;
  }
</style>
</head>
<body>
  <section class="card card-front">
    <h1 class="provider-name">Dr. Grant Morvel, D.O., P.A.</h1>
    <ul class="staff-list">
      <li>Board Certified Family Medicine</li>
      <li>Dr.Helena Morvel, DNP. Dr. Renata Ashby, DNP</li>
      <li>Dana Prewitt,APRN.Dr.Corinne Valdis, DNP</li>
      <li>Joyce Halvorsen,MSN, APRN-BC</li>
      <li>Dr. Lydia Thornquist,MD</li>
    </ul>
    <div class="brand">
      <span class="brand-dot"></span>
      <span class="brand-name">Morvel Family Medicine</span>
    </div>

    <address class="location location-primary">4815 Alder Rd. #220<br>Brookmere, FL 33010</address>
    <address class="location location-secondary">1750 N. Harbor Pkwy #201<br>Lakeview, FL 33020</address>

    <ul class="contact contact-left">
      <li><svg class="icon" viewBox="0 0 20 20"><path d="M2 8c0-3 4-4 8-4s8 1 8 4v1h-4V7H6v2H2zM5 10h10l2 6H3z"/></svg>555-010-4821</li>
      <li><svg class="icon" viewBox="0 0 20 20"><path d="M2 5h4v13H2zM7 2h9v5H7zM7 8h11v10H7z"/></svg>555-010-4822</li>
      <li><svg class="icon" viewBox="0 0 20 20"><path d="M2 7l8-5 8 5v11H2zM3 8l7 5 7-5"/></svg>office@doctormorvel.com</li>
    </ul>
    <ul class="contact contact-right">
      <li>555-010-7390<svg class="icon" viewBox="0 0 20 20"><path d="M2 8c0-3 4-4 8-4s8 1 8 4v1h-4V7H6v2H2zM5 10h10l2 6H3z"/></svg></li>
      <li>555-010-7391<svg class="icon" viewBox="0 0 20 20"><path d="M2 5h4v13H2zM7 2h9v5H7zM7 8h11v10H7z"/></svg></li>
      <li>www.DoctorMorvel.com<svg class="icon" viewBox="0 0 20 20"><circle cx="10" cy="10" r="8"/></svg></li>
    </ul>
  </section>

  <section class="card card-back">
    <h2 class="reminder-title">Your next appointment is scheduled for:</h2>
    <div class="field field-name"><span class="field-label">Name:</span><span class="field-line"></span></div>
    <div class="field field-date"><span class="field-label">Date:</span><span class="field-line"></span></div>
    <div class="field field-time"><span class="field-label">Time:</span><span class="field-line"></span></div>
    <p class="cancel-note">Please give 24 hours notice for cancellations to avoid a $50.00 no show fee.</p>
  </section>
</body>
</html>
```